Criminal Defense Firm looking for an edge in business card design

Established Criminal Defense Firm looking to refresh business card. We already have logo and website, but our business cards are extremely boring. We would like to also have something on the backside of card.
Needs to be business oriented, but creative.
We provide services to professionals such as doctors, lawyers, politicians, etc.
Our specialty is to protect professional licenses when facing a criminal matter.

Update on March 10, 2015: This project is for a Business Card Design. The winner in this project will be assigned the next (1on1) project which incidentally is also entitled Business Card Design. I'm sorry for this confusion. The 1on1 project will not be for Business Card Design but will be for Stationery-Envelope Design. Thank you for your attention and continued participation.

Target Market(s)

People accused of a crime

Industry/Entity Type

Business

Contact Information for Business Card

Simple, strong, professional

Colors
85abd2
3176b5
0355a3

```html
<!DOCTYPE html>
<html lang="en">
<head>
<meta charset="utf-8">
<title>Aldercott Vane Law Corporation – Business Cards</title>
<link rel="stylesheet" href="https://fonts.googleapis.com/css2?family=Open+Sans:wght@400;600;700&display=swap">
<style>
  :root {
    --backdrop: #4a3a34;
    --card: #2a2e31;
    --card-edge: #1f2225;
    --blue-light: #85abd2;
    --blue-mid: #3176b5;
    --blue-deep: #0355a3;
    --ink-soft: #9fb9d8;
    --ink-name: #b9cde4;
    --ink-dark: #0e1a28;
  }
  * { box-sizing: border-box; margin: 0; padding: 0; }
  html, body { width: 1200px; height: 768px; overflow: hidden; }
  body {
    background: var(--backdrop);
    font-family: "Open Sans", Arial, sans-serif;
    position: relative;
  }
  .card {
    position: absolute;
    width: 520px;
    height: 298px;
    background: var(--card);
    border: 1px solid var(--card-edge);
    overflow: hidden;
  }
  .card--back { left: 50px; top: 235px; }
  .card--front { left: 630px; top: 235px; }

  .band {
    position: absolute;
    left: 0; right: 0;
    height: 30px;
    background: linear-gradient(90deg, var(--blue-deep) 0%, var(--blue-mid) 30%, var(--blue-light) 55%, var(--blue-mid) 80%, var(--blue-deep) 100%);
    display: flex;
    align-items: center;
    color: var(--ink-dark);
    font-size: 13px;
    padding-left: 34px;
  }
  .card--back .band { top: 168px; }
  .card--front .band { top: 210px; font-size: 13.5px; padding-left: 22px; }

  /* back side mark */
  .back-mark {
    position: absolute;
    left: 0; right: 0; top: 44px;
    display: flex;
    flex-direction: column;
    align-items: center;
    gap: 12px;
  }
  .back-mark .dot {
    width: 78px; height: 78px;
    border: 4px solid var(--blue-mid);
    border-radius: 50%;
  }
  .firm-name {
    color: var(--blue-light);
    font-weight: 600;
    letter-spacing: 2px;
    text-transform: uppercase;
  }
  .back-mark .firm-name { font-size: 17px; }

  /* front side */
  .front-mark {
    position: absolute;
    left: 28px; top: 30px;
    display: flex;
    align-items: center;
    gap: 14px;
  }
  .front-mark .dot {
    width: 48px; height: 48px;
    border: 3px solid var(--blue-light);
    border-radius: 50%;
  }
  .front-mark .firm-name { font-size: 17px; line-height: 1.2; }
  .front-mark .firm-name small {
    display: block;
    font-size: 11px;
    letter-spacing: 1px;
    text-transform: none;
  }

  .contact-list {
    position: absolute;
    left: 28px; top: 132px;
    list-style: none;
    color: var(--ink-soft);
    font-size: 13.5px;
    line-height: 22px;
  }
  .contact-list li { display: flex; align-items: center; gap: 8px; }
  .contact-list svg { width: 13px; height: 13px; fill: var(--ink-soft); }

  .person {
    position: absolute;
    right: 24px; top: 148px;
    text-align: right;
  }
  .person-name { color: var(--ink-name); font-weight: 700; font-size: 18px; }
  .person-title { color: var(--ink-soft); font-size: 14px; margin-top: 2px; }
</style>
</head>
<body>

<section class="card card--back" aria-label="Card back">
  <div class="back-mark">
    <span class="dot"></span>
    <span class="firm-name">Aldercott Vane</span>
  </div>
  <div class="band">www.avdefenselaw.com</div>
</section>

<section class="card card--front" aria-label="Card front">
  <div class="front-mark">
    <span class="dot"></span>
    <span class="firm-name">Aldercott Vane<small>Law Corporation</small></span>
  </div>

  <ul class="contact-list">
    <li>
      <svg viewBox="0 0 16 16" aria-hidden="true"><path d="M2 4c0-1 1-2 2-2h8c1 0 2 1 2 2v2h-3V4H5v2H2zM3 7h10l1 7H2zM6 9v3h4V9z"/></svg>
      555-010-4821
    </li>
    <li>
      <svg viewBox="0 0 16 16" aria-hidden="true"><path d="M4 1h8v4H4zM1 6h14v6h-3v3H4v-3H1zM5 10v4h6v-4z"/></svg>
      555-010-4822
    </li>
    <li>
      <svg viewBox="0 0 16 16" aria-hidden="true"><path d="M1 3h14v10H1zM2 4.5v.5l6 4 6-4v-.5z"/></svg>
      daniel@avdefenselaw.com
    </li>
  </ul>

  <div class="person">
    <div class="person-name">Daniel Aldercott</div>
    <div class="person-title">Attorney at Law</div>
  </div>

  <div class="band">1180 Meridian Avenue, Suite 210 Marlow, California 90000</div>
</section>

</body>
</html>
```